Business card design needed

Business Card design required for new small plumbing business.
Would like a logo/text look that is simple and unique and does not have to be representative of a plumbing company (ie. having a cartoon plumber or toilet etc) as the companyname is self explanatory.
Would like the main colour to be green (lime green).
Updates

Industry/Entity Type

Plumber

Contact Information for Business Card

BRAVELL PLUMBING
ABN 61 904 127 558 003

Trevor Hasketh
Licensed Plumber 83615
Phone: 0412 870 245

27 Bravell Drive,
Marrowin. 3921 Eastland

Email: bravellplumbing@mailnest.example

Logo Text

Bravell Plumbing

Logo styles of interest
Character Logo
Wordmark Logo
Lettermark Logo

```html
<!DOCTYPE html>
<html lang="en">
<head>
<meta charset="utf-8">
<title>Bravell Plumbing – Business Card</title>
<link rel="stylesheet" href="https://fonts.googleapis.com/css2?family=Roboto+Slab:wght@700&family=Poiret+One&display=swap">
<style>
  :root {
    --paper: #ffffff;
    --green-lime: #a6c934;
    --rule: #c9e07c;
    --olive-text: #6f7f3c;
    --ink-grey: #5a5a5a;
    --abn-grey: #6a6a6a;
  }
  html, body {
    margin: 0;
    padding: 0;
    overflow: hidden;
    background: var(--paper);
  }
  .card {
    position: relative;
    width: 1200px;
    height: 741px;
    background: var(--paper);
    overflow: hidden;
  }
  .business-name {
    position: absolute;
    left: 58px;
    top: 120px;
    margin: 0;
    font-family: "Poiret One", "Century Gothic", sans-serif;
    font-weight: 400;
    font-size: 108px;
    line-height: 1;
    letter-spacing: 2px;
    color: var(--green-lime);
    white-space: nowrap;
  }
  .abn {
    position: absolute;
    left: 58px;
    top: 300px;
    margin: 0;
    font-family: "Poiret One", "Century Gothic", sans-serif;
    font-size: 44px;
    line-height: 1;
    color: var(--abn-grey);
    letter-spacing: 1px;
  }
  .rule {
    position: absolute;
    left: 0;
    top: 565px;
    width: 573px;
    height: 7px;
    background: var(--rule);
  }
  .contact {
    position: absolute;
    left: 598px;
    top: 440px;
  }
  .contact .person {
    margin: 0 0 4px;
    font-family: "Roboto Slab", Georgia, serif;
    font-weight: 700;
    font-size: 50px;
    line-height: 60px;
    color: var(--ink-grey);
  }
  .contact .details {
    margin: 0;
    font-family: "Poiret One", "Century Gothic", sans-serif;
    font-size: 31px;
    line-height: 41px;
    color: var(--olive-text);
    white-space: nowrap;
  }
</style>
</head>
<body>
  <div class="card">
    <h1 class="business-name">BRAVELL PLUMBING</h1>
    <p class="abn">ABN 61 904 127 558 003</p>

    <div class="rule"></div>

    <div class="contact">
      <p class="person">Trevor Hasketh</p>
      <p class="details">
        Licensed Plumber 83615<br>
        Bravell Drive, Marrowin. 3921 Eastland<br>
        Phone: 0412 870 245<br>
        Email: bravellplumbing@mailnest.example
      </p>
    </div>
  </div>
</body>
</html>
```